new pool company

I just started I pool service company last November based out of Winchester VA. My companies name is Brookstone Pool And Spa Service, LLC. I've been in the pool industry for 10 years. I want to build a customer base in my area.

I have an out of area telephone number so I want the postcard that I send out have something on it that lets people know I am a locally owned and operated company.

I also want it to say 'Licensed and Insured'

services provided (commercial and residential):
-Heater installs/diagnostics/repairs
-pool inspections
-electrical repairs
-plumbing repairs
-full system installations
-salt system conversions
-drain cleans w/ or w/ out acid
-pool closings
Lastly I want to feature the "pool openings" service on the card because that is the season that is coming.

The contact info I want displayed will be Kylemarsh@inboxly.example and my phone number at (555)-314-6027
Updates

I would like to see both side of the the card. I would also like pool openings to be more featured as a coming up service and not as a new service.

Must show both sides of card

Target Market(s)

I'm targeting upper middle class to upper class because of the obvious reasons of most pools are located in those areas.

Industry/Entity Type

Pool Service

Font styles to use
Serif
Sans Serif

Colors

Designer to choose colors to be used in the design.

Requirements
Must have
• Must have:
-Company name and contact info
-"Licensed and Insured"
-Logo that is attached
-"Locally owned and operated"

```html
<!DOCTYPE html>
<html lang="en">
<head>
<meta charset="utf-8">
<title>Brookstone Pool And Spa Service, LLC – Postcard</title>
<link rel="stylesheet" href="https://fonts.googleapis.com/css2?family=Lato:wght@400;700;900&display=swap">
<style>
  :root {
    --green-dark: #3c8a2c;
    --green-mid: #5fa83a;
    --green-light: #8cc63f;
    --yellow: #ffe600;
    --ink: #2b2b2b;
    --ink-green: #2f6e27;
    --white: #ffffff;
    --page: #e9e9e9;
    --pool: #3fb8e0;
    --sky: #a9c9e6;
  }
  * { margin: 0; padding: 0; box-sizing: border-box; }
  html, body { width: 866px; height: 1200px; overflow: hidden; }
  body {
    background: var(--page);
    font-family: "Lato", Arial, sans-serif;
    position: relative;
  }
  .postcard {
    position: absolute;
    left: 83px;
    width: 700px;
    height: 541px;
    overflow: hidden;
    background: var(--white);
    box-shadow: 0 3px 10px rgba(0,0,0,.25);
  }
  .postcard--front { top: 22px; }
  .postcard--back { top: 623px; }
  .postcard svg.layer { position: absolute; inset: 0; width: 100%; height: 100%; }

  /* front */
  .experience {
    position: absolute; left: 0; width: 362px; top: 50px;
    text-align: center; color: var(--white);
  }
  .experience__main { font-weight: 900; font-size: 24px; letter-spacing: .3px; }
  .experience__main span { color: var(--yellow); }
  .experience__sub { font-weight: 400; font-size: 19px; margin-top: 2px; }
  .brand-mark {
    position: absolute; left: 94px; top: 179px; width: 126px; height: 126px;
    border-radius: 50%; background: var(--white); border: 8px solid var(--green-mid);
  }
  .brand-name {
    position: absolute; left: 30px; top: 330px; width: 340px; white-space: nowrap;
  }
  .brand-name__line1 { font-size: 32px; color: var(--ink-green); line-height: 1.1; }
  .brand-name__line2 { font-size: 32px; color: var(--ink); line-height: 1.2; }
  .brand-name__rule { height: 2px; background: var(--ink); margin: 8px 0 6px; width: 260px; }
  .brand-name__tag { font-size: 20px; color: var(--ink); padding-left: 20px; }
  .local-note {
    position: absolute; left: 0; width: 400px; top: 502px;
    text-align: center; color: var(--white);
    font-weight: 900; font-size: 17px; letter-spacing: 1px;
  }

  /* back */
  .season-note {
    position: absolute; left: 36px; top: 22px; width: 380px;
    color: var(--yellow); font-weight: 900; font-size: 17px; text-align: center;
  }
  .offer-pill {
    position: absolute; left: 136px; top: 59px; width: 152px; height: 33px;
    border-radius: 17px; background: var(--yellow);
    color: var(--ink-green); font-weight: 900; font-size: 21px;
    text-align: center; line-height: 33px;
  }
  .services { position: absolute; list-style: none; }
  .services--left { left: 36px; top: 130px; width: 230px; }
  .services--right { left: 275px; top: 130px; width: 200px; }
  .services li {
    position: relative; padding-left: 18px;
    font-weight: 700; font-size: 19px; line-height: 25px; color: var(--ink);
  }
  .services li::before {
    content: ""; position: absolute; left: 0; top: 9px;
    width: 9px; height: 9px; border-radius: 50%; background: var(--yellow);
  }
  .services--left li { margin-bottom: 9px; }
  .services--left li:nth-child(3) { margin-bottom: 18px; }
  .services--right li { margin-bottom: 10px; }

  .footer-mark {
    position: absolute; left: 66px; top: 360px; width: 82px; height: 82px;
    border-radius: 50%; background: var(--white); border: 5px solid var(--yellow);
  }
  .footer-name { position: absolute; left: 165px; top: 372px; width: 180px; white-space: nowrap; }
  .footer-name__line1 { font-size: 16px; color: var(--yellow); line-height: 1.25; }
  .footer-name__line2 { font-size: 16px; color: var(--white); line-height: 1.25; }
  .footer-name__rule { height: 1.5px; background: var(--ink); margin: 3px 0 3px; width: 140px; }
  .footer-name__tag { font-size: 11px; color: var(--ink); padding-left: 10px; }

  .contact { position: absolute; left: 36px; list-style: none; color: var(--white); font-weight: 700; font-size: 18px; }
  .contact li { display: flex; align-items: center; gap: 10px; height: 30px; }
  .contact svg { width: 16px; height: 16px; flex: none; }
  .contact--list { top: 460px; }

  .stamp-box {
    position: absolute; left: 582px; top: 75px; width: 86px; height: 98px;
    border: 1.5px solid var(--ink);
  }
  .address-line { position: absolute; left: 518px; width: 150px; height: 2px; background: var(--ink); }
</style>
</head>
<body>

<section class="postcard postcard--front" aria-label="Postcard front">
  <svg class="layer" viewBox="0 0 700 541" aria-hidden="true">
    <defs>
      <linearGradient id="frontYellow" x1="0" y1="0" x2="1" y2="0">
        <stop offset="0" stop-color="#ffd200"/><stop offset="1" stop-color="#fff200"/>
      </linearGradient>
      <linearGradient id="frontGreen" x1="0" y1="0" x2="1" y2="0">
        <stop offset="0" stop-color="#4f9a33"/><stop offset="1" stop-color="#8cc63f"/>
      </linearGradient>
    </defs>
    <rect width="700" height="541" fill="url(#frontYellow)"/>
    <rect width="700" height="158" fill="url(#frontGreen)"/>
    <rect y="486" width="700" height="55" fill="url(#frontGreen)"/>
    <path d="M415 0 Q340 270 452 541" fill="none" stroke="var(--yellow)" stroke-width="14"/>
  </svg>
  <svg class="layer" viewBox="0 0 700 541" role="img" aria-label="Photo of a resort building beside a large blue swimming pool with palm trees">
    <defs>
      <linearGradient id="poolPhoto" x1="0" y1="0" x2="0" y2="1">
        <stop offset="0" stop-color="var(--sky)"/>
        <stop offset=".45" stop-color="#d9d7cf"/>
        <stop offset=".62" stop-color="#5fa055"/>
        <stop offset=".72" stop-color="var(--pool)"/>
        <stop offset="1" stop-color="#2fa6d6"/>
      </linearGradient>
    </defs>
    <path d="M422 0 Q348 270 459 541 L700 541 L700 0 Z" fill="url(#poolPhoto)"/>
  </svg>

  <div class="experience">
    <p class="experience__main"><span>10 YEARS</span> OF EXPERIENCE</p>
    <p class="experience__sub">IN POOL SERVICE</p>
  </div>
  <div class="brand-mark" aria-hidden="true"></div>
  <div class="brand-name">
    <p class="brand-name__line1">Brookstone Pool And</p>
    <p class="brand-name__line2">Spa Service, LLC.</p>
    <div class="brand-name__rule"></div>
    <p class="brand-name__tag">Licensed and Insured</p>
  </div>
  <p class="local-note">LOCALLY OWNED AND OPERATED</p>
</section>

<section class="postcard postcard--back" aria-label="Postcard back">
  <svg class="layer" viewBox="0 0 700 541" aria-hidden="true">
    <defs>
      <linearGradient id="backGreen" x1="0" y1="0" x2="1" y2="0">
        <stop offset="0" stop-color="#5fae3a"/><stop offset=".35" stop-color="#8cc63f"/><stop offset="1" stop-color="#3c8a2c"/>
      </linearGradient>
    </defs>
    <path d="M0 0 L421 0 Q520 270 421 541 L0 541 Z" fill="url(#backGreen)"/>
    <path d="M421 0 Q520 270 421 541" fill="none" stroke="var(--yellow)" stroke-width="8"/>
  </svg>

  <p class="season-note">Now booking spring pool openings!</p>
  <div class="offer-pill">WE OFFER</div>
  <ul class="services services--left">
    <li>Heater install<br>/diagnostics/repairs</li>
    <li>Pool inspections</li>
    <li>Electrical repairs</li>
    <li>Plumbing repairs</li>
    <li>Pool closings</li>
  </ul>
  <ul class="services services--right">
    <li>Full system<br>installations</li>
    <li>Salt system<br>conversions</li>
    <li>Drain cleans<br>w/ or w/ out acid</li>
  </ul>

  <div class="footer-mark" aria-hidden="true"></div>
  <div class="footer-name">
    <p class="footer-name__line1">Brookstone Pool And</p>
    <p class="footer-name__line2">Spa Service, LLC.</p>
    <div class="footer-name__rule"></div>
    <p class="footer-name__tag">Licensed and Insured</p>
  </div>

  <ul class="contact contact--list">
    <li>
      <svg viewBox="0 0 16 16" aria-hidden="true"><path d="M3 1 L6 1 L7 5 L5 6.5 Q6.5 9.5 9.5 11 L11 9 L15 10 L15 13 Q15 15 13 15 Q1 14 1 3 Q1 1 3 1 Z" fill="var(--yellow)"/></svg>
      <span>(555)-314-6027</span>
    </li>
    <li>
      <svg viewBox="0 0 16 16" aria-hidden="true"><rect x="1" y="3" width="14" height="10" fill="var(--yellow)"/><path d="M1 3 L8 9 L15 3" fill="none" stroke="var(--green-dark)" stroke-width="1.3"/></svg>
      <span>Kylemarsh@inboxly.example</span>
    </li>
  </ul>

  <svg class="layer" viewBox="0 0 700 541" role="img" aria-label="Round photo of a pool technician cleaning a swimming pool">
    <defs>
      <linearGradient id="techPhoto" x1="0" y1="0" x2="0" y2="1">
        <stop offset="0" stop-color="#8fb3cf"/><stop offset=".45" stop-color="#c9c3b4"/><stop offset="1" stop-color="#3fa8d4"/>
      </linearGradient>
    </defs>
    <circle cx="434" cy="420" r="74" fill="url(#techPhoto)" stroke="var(--yellow)" stroke-width="7"/>
  </svg>

  <div class="stamp-box" aria-hidden="true"></div>
  <div class="address-line" style="top:258px" aria-hidden="true"></div>
  <div class="address-line" style="top:293px" aria-hidden="true"></div>
  <div class="address-line" style="top:334px" aria-hidden="true"></div>
</section>

</body>
</html>
```